Keystone Prime Water Tank

I primarily market the water tanks so want a business care that reflects that. I have attached the water tank logo. You have been working on our water tank so maybe we can use that on the card et. I am leaving as one sided but can be double sided if that works. The information that needs to be on the cards is as follows: Gerald T. Munro Phone numbers: Office 555-284-9137 Direct 555-619-2405 Mobile 555-372-5841 email address: gerald@fieldgearworks.com Address P.O. Box 8273 Maplecrest, GA 30512 Web Page: www.fieldgearworks.com. A lot to fit on the card. Thanks

```html
<!DOCTYPE html>
<html lang="en">
<head>
<meta charset="utf-8">
<title>Keystone Prime Water Tank – Business Card</title>
<link href="https://fonts.googleapis.com/css2?family=Arimo:wght@400;700&display=swap" rel="stylesheet">
<style>
  :root {
    --brand-red: #e30613;
    --ink: #1a1a1a;
    --card: #ffffff;
    --backdrop: #d9d9d9;
    --font-main: "Arimo", Arial, sans-serif;
  }
  * { margin: 0; padding: 0; box-sizing: border-box; }
  html, body {
    width: 1200px;
    height: 900px;
    overflow: hidden;
    background: var(--backdrop);
    font-family: var(--font-main);
  }
  .canvas {
    width: 1200px;
    height: 900px;
    display: flex;
    align-items: center;
    justify-content: center;
  }
  .business-card {
    position: relative;
    width: 1000px;
    height: 572px;
    background: var(--card);
    border-bottom: 16px solid var(--brand-red);
    box-shadow: 0 18px 40px rgba(0, 0, 0, 0.25);
    color: var(--ink);
  }
  .brand {
    position: absolute;
    left: 70px;
    top: 150px;
    display: flex;
    align-items: center;
    gap: 14px;
  }
  .brand-mark {
    width: 34px;
    height: 34px;
    background: var(--brand-red);
  }
  .brand-name {
    font-size: 30px;
    font-weight: 700;
    color: var(--ink);
    line-height: 1.1;
    width: 260px;
  }
  .identity {
    position: absolute;
    right: 150px;
    top: 100px;
    text-align: right;
  }
  .identity-name {
    font-size: 50px;
    font-weight: 700;
    color: var(--brand-red);
    letter-spacing: 0.5px;
  }
  .identity-title {
    font-size: 26px;
    color: var(--ink);
    margin-top: 2px;
  }
  .contact-list {
    position: absolute;
    left: 440px;
    top: 300px;
    list-style: none;
    font-size: 25px;
    line-height: 1.22;
  }
  .contact-label {
    color: var(--brand-red);
    font-weight: 700;
  }
  .postal-address {
    position: absolute;
    left: 440px;
    top: 478px;
    font-size: 25px;
  }
  .postal-address strong { font-weight: 700; }
</style>
</head>
<body>
  <main class="canvas">
    <article class="business-card">
      <div class="brand">
        <span class="brand-mark"></span>
        <span class="brand-name">Keystone Prime Water Tank</span>
      </div>

      <header class="identity">
        <h1 class="identity-name">Gerald T. Munro</h1>
        <p class="identity-title">Director</p>
      </header>

      <ul class="contact-list">
        <li><span class="contact-label">Office:</span> 555-284-9137</li>
        <li><span class="contact-label">Direct:</span> 555-619-2405</li>
        <li><span class="contact-label">Mobile:</span> 555-372-5841</li>
        <li><span class="contact-label">Email:</span> gerald@fieldgearworks.com</li>
        <li><span class="contact-label">Web:</span> www.fieldgearworks.com</li>
      </ul>

      <p class="postal-address"><strong>P.O. Box</strong> 8273 Maplecrest, GA 30512</p>
    </article>
  </main>
</body>
</html>
```